Business card design needed

New company in Executive Search & Consulting (Recruitment & Head Hunting Company)

We recruit IT, Accounting & Finance, Human Resources and Senior Management

with offices in Perth, Brisbane, Seoul and Hong Kong

Industry/Entity Type

Business

Contact Information for Business Card

Calderwood-Ashfield Executive Search & Consulting
*Perth *Brisbane * Seoul * Hong Kong
Neil Calderwood Australian Director
147 Mellor Street Subiaco Western Australia
www.calderwoodashfield.example.au
Ph: 08 6000 4827 Fax: 08 6000 9153
Mobile: 0400 731 562

```html
<!DOCTYPE html>
<html lang="en">
<head>
<meta charset="utf-8">
<title>Calderwood-Ashfield Business Card</title>
<link rel="stylesheet" href="https://fonts.googleapis.com/css2?family=Cinzel:wght@400;500&family=PT+Sans+Narrow&display=swap">
<style>
  :root {
    --page: #ececec;
    --card-white: #ffffff;
    --slate: #535c66;
    --slate-light: #8a929c;
    --slate-faint: #5c656f;
    --ink: #4a525b;
    --text-light: #f2f3f5;
    --mark-grey: #d5d8dc;
  }
  * { margin: 0; padding: 0; box-sizing: border-box; }
  html, body { width: 1200px; height: 900px; overflow: hidden; }
  body {
    background: radial-gradient(circle at 50% 45%, #fafafa 0%, var(--page) 70%, #d9d9d9 100%);
    position: relative;
  }
  .card {
    position: absolute;
    width: 560px;
    height: 320px;
    overflow: hidden;
    box-shadow: 0 6px 18px rgba(0,0,0,0.18);
  }
  .card--front { left: 130px; top: 90px; background: var(--card-white); }
  .card--back { left: 510px; top: 480px; background: var(--slate); }

  .front__band { position: absolute; inset: 0; }
  .front__mark {
    position: absolute;
    left: 248px; top: 30px;
    width: 64px; height: 64px;
    border-radius: 50%;
    background: var(--mark-grey);
  }
  .front__name {
    position: absolute;
    left: 0; right: 0; top: 110px;
    text-align: center;
    font-family: "Cinzel", serif;
    font-size: 30px;
    font-weight: 400;
    color: var(--ink);
    letter-spacing: 0.5px;
  }
  .front__tagline {
    position: absolute;
    left: 0; right: 0; top: 152px;
    text-align: center;
    font-family: "Cinzel", serif;
    font-size: 15px;
    color: var(--ink);
    letter-spacing: 1px;
  }
  .front__offices {
    position: absolute;
    left: 0; right: 0; top: 274px;
    text-align: center;
    font-family: "PT Sans Narrow", sans-serif;
    font-size: 19px;
    color: var(--text-light);
    letter-spacing: 0.3px;
  }

  .back__decor {
    position: absolute;
    left: 24px; top: 150px;
    font-family: "Cinzel", serif;
    font-size: 20px;
    color: var(--slate-faint);
  }
  .back__details {
    position: absolute;
    right: 40px; top: 34px;
    text-align: right;
    color: var(--text-light);
  }
  .back__person {
    font-family: "Cinzel", serif;
    font-size: 22px;
    font-weight: 500;
    letter-spacing: 0.5px;
  }
  .back__role {
    font-family: "Cinzel", serif;
    font-size: 16px;
    font-weight: 400;
    letter-spacing: 0.8px;
    margin-top: 4px;
  }
  .back__contact {
    margin-top: 40px;
    font-family: "PT Sans Narrow", sans-serif;
    font-size: 18px;
    line-height: 24px;
    list-style: none;
  }
</style>
</head>
<body>
  <section class="card card--front">
    <svg class="front__band" width="560" height="320" viewBox="0 0 560 320" aria-hidden="true">
      <path d="M0 226 Q320 232 560 184 L560 320 L0 320 Z" fill="var(--slate-light)"/>
      <path d="M0 238 Q320 244 560 196 L560 320 L0 320 Z" fill="var(--slate)"/>
    </svg>
    <div class="front__mark"></div>
    <h1 class="front__name">Calderwood-Ashfield</h1>
    <p class="front__tagline">EXECUTIVE SEARCH &amp; CONSULTING</p>
    <p class="front__offices">PERTH • BRISBANE • SEOUL • HONG KONG</p>
  </section>

  <section class="card card--back">
    <div class="back__decor">Calderwood-Ashfield</div>
    <div class="back__details">
      <h2 class="back__person">Neil Calderwood</h2>
      <p class="back__role">Australian Director</p>
      <ul class="back__contact">
        <li>147 Mellor Street Subiaco,</li>
        <li>Western Australia</li>
        <li>www.calderwoodashfield.example.au</li>
        <li>Ph: 08 6000 4827</li>
        <li>Fax: 08 6000 9153</li>
        <li>Mobile: 0400 731 562</li>
      </ul>
    </div>
  </section>
</body>
</html>
```